mechanical repair shop

our shop repairs light and medium duty trucks

we sell tires , do oil changes, engine and transmissions
vehicle accessories, alignments, brakes , exhaust, all major and minor repairs.

if you would like to get a hold of me email: kelvin.moraday@quillstenworks.com tel: 1-555-418-3067

Target Market(s)

light and medium duty trucks and cars

Industry/Entity Type

Shop

Colors
f37122

Requirements
Must have
• visual sales displays
Nice to have
• pictures

```html
<!DOCTYPE html>
<html lang="en">
<head>
<meta charset="utf-8">
<title>Quillsten Works – Truck Repair Flyer</title>
<link href="https://fonts.googleapis.com/css2?family=Oswald:wght@400;500;700&family=Montserrat:wght@400;500;600&display=swap" rel="stylesheet">
<style>
  :root{
    --orange:#f37122;
    --orange-deep:#e0561a;
    --black:#0d0d0d;
    --white:#ffffff;
    --ink:#222222;
    --backdrop:#3a3a3a;
  }
  *{box-sizing:border-box;margin:0;padding:0}
  html,body{width:1200px;height:900px;overflow:hidden;background:var(--backdrop)}
  .flyer{position:absolute;left:296px;top:20px;width:608px;height:860px;background:var(--white);overflow:hidden;font-family:"Montserrat",sans-serif;color:var(--ink)}
  .layer{position:absolute;left:0;top:0}
  .brand{position:absolute;left:34px;top:120px;width:200px;display:flex;align-items:center;gap:10px}
  .brand-dot{width:18px;height:18px;border-radius:50%;background:var(--orange);flex:none}
  .brand-name{font-family:"Montserrat",sans-serif;font-weight:600;font-size:19px;line-height:1.15;color:var(--white)}
  .brand-tag{position:absolute;left:62px;top:172px;font-size:8px;font-weight:600;color:var(--orange);letter-spacing:.2px}
  .truck-photo{position:absolute;left:250px;top:54px;width:300px;height:190px;border-radius:4px;background:linear-gradient(160deg,#f4f4f4 0%,#d9d9d9 60%,#9a9a9a 100%)}
  .headline{position:absolute;right:30px;top:262px;text-align:right;font-family:"Oswald",sans-serif;font-weight:700;font-size:31px;line-height:1.05;letter-spacing:-.5px;text-transform:uppercase;color:var(--white)}
  .headline .dark{color:var(--black)}
  .services{position:absolute;left:30px;top:372px;width:290px}
  .services h2{font-family:"Oswald",sans-serif;font-weight:500;font-size:27px;color:var(--orange);margin-bottom:10px}
  .services ul{list-style:none}
  .services li{display:flex;align-items:center;gap:8px;font-size:11.5px;line-height:21.6px;color:var(--ink)}
  .services svg{width:11px;height:11px;flex:none}
  .photo-row{position:absolute;left:330px;top:372px;width:254px;height:132px;display:flex;gap:4px}
  .photo{flex:1}
  .photo-tires{background:linear-gradient(150deg,#6a6a6a,#1e1e1e)}
  .photo-oil{background:linear-gradient(150deg,#b9b9b9,#4c4c4c 60%,#c78a1a)}
  .about{position:absolute;left:330px;top:516px;width:254px;font-size:10px;line-height:15.5px;text-align:justify;color:var(--ink)}
  .website{position:absolute;right:20px;top:740px;font-family:"Oswald",sans-serif;font-size:17px;color:var(--white)}
  .contact{position:absolute;left:40px;top:780px;color:var(--white)}
  .contact-label{font-family:"Oswald",sans-serif;font-weight:500;font-size:17px;color:var(--orange)}
  .contact-phone{display:flex;align-items:center;gap:8px;font-family:"Oswald",sans-serif;font-weight:400;font-size:36px;line-height:1.1}
  .contact-phone svg{width:26px;height:26px}
</style>
</head>
<body>
<svg width="0" height="0" style="position:absolute">
  <symbol id="tick" viewBox="0 0 12 12">
    <circle cx="6" cy="6" r="5" fill="none" stroke="#f37122" stroke-width="1.4"/>
    <path d="M3.4 6.2 5.3 8 8.8 4.2" fill="none" stroke="#f37122" stroke-width="1.5" stroke-linecap="round" stroke-linejoin="round"/>
  </symbol>
</svg>

<main class="flyer">
  <svg class="layer" width="608" height="860" viewBox="0 0 608 860" aria-hidden="true">
    <defs>
      <linearGradient id="orangeBand" x1="0" y1="1" x2="1" y2="0">
        <stop offset="0" stop-color="#f58a2e"/>
        <stop offset="1" stop-color="#e0561a"/>
      </linearGradient>
    </defs>
    <rect x="0" y="0" width="608" height="350" fill="#0d0d0d"/>
    <polygon points="0,345 560,0 608,0 608,345" fill="url(#orangeBand)"/>
    <polygon points="478,0 540,0 430,68" fill="#ffffff"/>
    <polygon points="0,345 608,345 608,352 0,360" fill="#ffffff"/>
    <polygon points="560,352 608,350 608,380" fill="#0d0d0d"/>
    <polygon points="330,760 608,690 608,760" fill="#e0561a"/>
    <polygon points="0,738 608,760 608,860 0,860" fill="#0d0d0d"/>
  </svg>

  <div class="brand">
    <span class="brand-dot"></span>
    <span class="brand-name">Quillsten Works Ltd.</span>
  </div>
  <div class="brand-tag">Oilfield Services &amp; Maintenance</div>

  <div class="truck-photo" role="img" aria-label="White light-duty box truck"></div>

  <h1 class="headline">Your complete <span class="dark">light &amp; medium</span><br><span class="dark">duty</span> truck repair facility</h1>

  <section class="services">
    <h2>Services We Offer:</h2>
    <ul>
      <li><svg><use href="#tick"/></svg>Factory recommended service/maintenance</li>
      <li><svg><use href="#tick"/></svg>Oil change</li>
      <li><svg><use href="#tick"/></svg>Fuel system repair and maintenance</li>
      <li><svg><use href="#tick"/></svg>Battery system diagnosis &amp; repair</li>
      <li><svg><use href="#tick"/></svg>Check engine light</li>
      <li><svg><use href="#tick"/></svg>Electrical problems</li>
      <li><svg><use href="#tick"/></svg>Engine performance</li>
      <li><svg><use href="#tick"/></svg>Exhaust problems</li>
      <li><svg><use href="#tick"/></svg>Tires</li>
      <li><svg><use href="#tick"/></svg>30/60/90 K mileage maintenance services</li>
      <li><svg><use href="#tick"/></svg>Cooling system repair and maintenance</li>
      <li><svg><use href="#tick"/></svg>Air conditioning / heating repair</li>
      <li><svg><use href="#tick"/></svg>Brake system</li>
      <li><svg><use href="#tick"/></svg>Steering &amp; suspension</li>
    </ul>
  </section>

  <div class="photo-row">
    <div class="photo photo-tires" role="img" aria-label="Mechanic mounting a truck tire"></div>
    <div class="photo photo-oil" role="img" aria-label="Fresh oil being poured into an engine"></div>
  </div>

  <p class="about">Quillsten Works Ltd. has set up and successfully operates a complete equipment repair facility. First set up to be a dedicated repair shop for a single large client, Quillsten has now expanded to include all manner of clients with diverse equipment needs. With Journeyman and Apprentice HD mechanics available 24 hours a day our facility is ready to handle all of your equipment needs. We are an ‘approved’ repair facility for a growing list of equipment manufacturers including: Ridgeline, Carrow, Tallis, Bexmoor, Stratalift etc.</p>

  <div class="website">www.quillstenworks.com</div>

  <footer class="contact">
    <div class="contact-label">Call us for more information</div>
    <div class="contact-phone">
      <svg viewBox="0 0 24 24" aria-hidden="true"><path fill="#ffffff" d="M6.6 10.8a15.1 15.1 0 0 0 6.6 6.6l2.2-2.2c.3-.3.7-.4 1-.2 1.1.4 2.3.6 3.6.6.6 0 1 .4 1 1V20c0 .6-.4 1-1 1A17 17 0 0 1 3 4c0-.6.4-1 1-1h3.5c.6 0 1 .4 1 1 0 1.3.2 2.5.6 3.6.1.3 0 .7-.2 1z"/></svg>
      <span>555 418 3067</span>
    </div>
  </footer>
</main>
</body>
</html>
```